Flyer for "Master the Mash Tun Basics" course

NEEDED: A6 flyer designed to advertise my first training course:
Intro to craft beer brewing

The company brand identity was recently bought from Pixel Harbor and it can be seen, with colour scheme on our website: www.TinmoorKettle.com.

The flyer is to be in line with my current brand identity and have a strong hook to push people to our site.

The flyer's goal is to get people to visit the site to book on a craft beer brewing training course. The info available to be included, although you have the freedom to include as much or as little as you see fit:

Currently a sale of 60% off on the course cost
RRP £120 Sale Price £50 (limited time only)
Courses will be run in central London
The website is TinmoorKettle.com
Hands on, half day course, brunch and a couple of sample beers included
Dates available:
14th December 2014
11th January 2015
18th January 2015
25th January 2015
1st February 2015
8th February 2015
15th February 2015
22nd February 2015

Logo file included, AI version available on request. Any photo on the TinmoorKettle.com site is available to be used. Simply pull of the site or I can send to you.

Colour scheme used on site: #FF9700 & #26210D

I will reply to any designs offered between 8pm and 11pm BST each day.

Good luch!

Hi everyone, We have now reviewed the first submissions and there are some ok, some good and a couple of great efforts in there. Here are the following common things that we commented on in our first reviews: 1. WHAT IS THE FLYER TRYING TO SAY... YOU'VE GOT 1 SECOND!!!! This flyer is to be given out in the street. That gives you 1second to tell the reader what the flyer is selling. That is the number 1 priority for the flyer. Please make it your priority as designers. 2. SALE SALE SALE This is the number 2 priority, people love SALES and a big colourful sticker saying SALE or 60% OFF (or both) is to be positioned so once the reader has seen that the flyer is about a craft beer brewing course, they see there is a sale on the course. 3. BRAND PERSONALITY 3rd priority is the Tinmoor Kettle brand identity. We picked this name, logo and colour scheme to stand out. Please use these to enhance points 1 & 2, but also get our logo on there is a bold and brash way. 4. USE THE BACK OF THE CARD Place any info that is not required in 1, 2 & 3 on the back, or even remove it all together if YOU feel it is not suited. You are the designer, so make some design decisions! We are happy to ask you to add things back in if we feel it is lacking. Our best guess (and we are NOT designers) is that putting either the dates OR a brief description of the course on the back would be enough info. If you think we can get bother, without overloading the page, give it a go! 5. CALL TO ACTION On the front and on the back, we want a CALL TO ACTION. Book at TinmoorKettle.com or just TinmoorKettle.com (you do not need http://www before it!!! We live in 2014 not 1994!!!) 6. MAKE IT BOLD, & THEN MAKE IT BOLDER This flyer is to stand out to a person that is handed 1 different leaflet every 2 minutes while walking down a busy London high street. We MUST stand out. Finally, thanks for all the designer so far, your efforts are greatly appreciated and we are very excited about the new revision of the design!

Target Market(s)

City living, young professionals who like to do fun things at the weekend.

Industry/Entity Type

Training

Font styles to use
Sans Serif

Colors
f78f20

Requirements
Must have
• Strong brand identity and call to action
In line with brand identity, see website www.TinmoorKettle.com

```html
<!DOCTYPE html>
<html lang="en">
<head>
<meta charset="utf-8">
<title>Tinmoor Kettle – Learn to Brew</title>
<link rel="stylesheet" href="https://fonts.googleapis.com/css2?family=Open+Sans:wght@400;600;800&family=Arimo:ital,wght@0,400;0,700;1,400;1,700&display=swap">
<style>
  :root {
    --brand-orange: #ff9700;
    --brand-dark: #26210d;
    --ink: #1c1a14;
    --sale-red: #ff0a0a;
    --accent-red: #e8231c;
    --white: #ffffff;
    --photo-light: #f3ece2;
    --photo-mid: #d9c7a6;
    --photo-warm: #c99a55;
  }
  * { margin: 0; padding: 0; box-sizing: border-box; }
  html, body { width: 851px; height: 1200px; overflow: hidden; background: var(--white); }
  .flyer {
    position: relative;
    width: 851px;
    height: 1200px;
    overflow: hidden;
    font-family: "Arimo", Arial, sans-serif;
    color: var(--ink);
  }

  /* Header band */
  .brand-band {
    position: absolute; left: 0; top: 0; width: 851px; height: 150px;
    background: var(--brand-orange);
  }
  .brand-mark {
    position: absolute; left: 42px; top: 30px; width: 94px; height: 94px;
    border-radius: 50%; background: var(--brand-dark);
  }
  .brand-name {
    position: absolute; left: 160px; top: 36px; width: 670px;
    font-family: "Open Sans", sans-serif; font-weight: 800;
    font-size: 70px; line-height: 80px; letter-spacing: 0.5px;
    color: var(--ink); text-transform: uppercase; white-space: nowrap;
  }

  /* Hero */
  .hero-photo {
    position: absolute; left: 0; top: 150px; width: 851px; height: 467px;
    background:
      radial-gradient(ellipse at 75% 40%, rgba(201,154,85,0.45), transparent 60%),
      radial-gradient(ellipse at 30% 60%, rgba(217,199,166,0.7), transparent 65%),
      linear-gradient(180deg, var(--photo-light) 0%, var(--photo-mid) 100%);
  }
  .hero-title {
    position: absolute; left: 22px; top: 228px;
    font-size: 96px; line-height: 104px; font-weight: 400;
    color: var(--ink); white-space: nowrap;
  }
  .hero-title em { font-style: italic; }
  .hero-subtitle {
    position: absolute; left: 24px; top: 338px;
    font-size: 32px; line-height: 38px; color: var(--ink);
  }

  /* Offer panel */
  .offer-panel {
    position: absolute; left: 0; top: 617px; width: 851px; height: 414px;
    background: var(--brand-dark);
  }
  .sale-sticker {
    position: absolute; left: 631px; top: 524px; width: 192px; height: 192px;
  }
  .sale-sticker-label {
    position: absolute; left: 631px; top: 586px; width: 192px; text-align: center;
    font-size: 60px; line-height: 64px; font-style: italic; font-weight: 700;
    color: var(--ink);
  }
  .offer-details {
    position: absolute; left: 24px; top: 722px; width: 590px; color: var(--white);
  }
  .offer-price {
    font-size: 32px; line-height: 38px; white-space: nowrap;
  }
  .offer-price .discount,
  .offer-price .sale-price { color: var(--accent-red); font-style: italic; font-weight: 700; }
  .offer-price .rrp-old { text-decoration: line-through; }
  .offer-limit { font-size: 32px; line-height: 38px; }
  .offer-copy {
    margin-top: 2px; font-size: 21.5px; line-height: 32.5px; text-align: justify;
  }
  .offer-copy em { color: var(--accent-red); font-style: italic; }

  .course-dates {
    position: absolute; left: 620px; top: 720px; width: 210px;
    text-align: center; color: var(--white);
    font-size: 22.5px; line-height: 29.6px; list-style: none;
  }

  /* Footer call to action */
  .cta-band {
    position: absolute; left: 0; top: 1031px; width: 851px; height: 169px;
    background: var(--brand-orange);
  }
  .cta-text {
    position: absolute; left: 0; top: 1088px; width: 851px; text-align: center;
    font-family: "Open Sans", sans-serif; font-weight: 400;
    font-size: 30px; line-height: 38px; color: var(--ink);
  }
</style>
</head>
<body>
<div class="flyer">
  <header class="brand-band">
    <div class="brand-mark"></div>
    <div class="brand-name">Tinmoor Kettle</div>
  </header>

  <section class="hero">
    <div class="hero-photo" role="img" aria-label="Photo of smiling friends raising pint glasses of pale beer in a toast"></div>
    <h1 class="hero-title"><em>Learn</em> to Brew!</h1>
    <p class="hero-subtitle">Intro to craft beer brewing course</p>
  </section>

  <section class="offer-panel"></section>

  <svg class="sale-sticker" viewBox="0 0 192 192" aria-hidden="true">
    <circle cx="96" cy="96" r="96" fill="var(--sale-red)"/>
  </svg>
  <div class="sale-sticker-label">SALE!</div>

  <div class="offer-details">
    <p class="offer-price"><span class="discount">60% OFF</span> RRP <span class="rrp-old">£120</span> <span class="sale-price">£50</span></p>
    <p class="offer-limit">(Limited time only)</p>
    <p class="offer-copy">A hands on, half day, intro to beer brewing course. The half day includes a <em>full English breakfast</em>, a <em>sample beer</em> and 3 of the beers brewed on the day to take away to enjoy when it comes into condition. The courses will be run in central London.</p>
  </div>

  <ul class="course-dates">
    <li>Available Dates</li>
    <li>14th Dec. 2014</li>
    <li>11th Jan. 2015</li>
    <li>18th Jan. 2015</li>
    <li>25th Jan. 2015</li>
    <li>1st Feb. 2015</li>
    <li>8th Feb. 2015</li>
    <li>15th Feb. 2015</li>
    <li>22nd Feb. 2015</li>
  </ul>

  <footer class="cta-band"></footer>
  <p class="cta-text">Register at TinmoorKettle.com</p>
</div>
</body>
</html>
```